PebbleLoop screens tidy up

We would like advice on how to better present the following home page and overview pages.

The existing website is functional, but the pages don't appear professionals and pleasing to the eye. We would specifically like feedback on alignment and padding of icons and text to make the screen more appealing and polished.

We are following the quartz design system.

Number of Pages Required

1 page

Font styles to use
Sans Serif
Other font styles liked:
• IBM Plex, Poppins

```html
<!DOCTYPE html>
<html lang="en">
<head>
<meta charset="utf-8">
<title>PebbleLoop – Overview</title>
<link href="https://fonts.googleapis.com/css2?family=Lato:wght@400;700&display=swap" rel="stylesheet">
<style>
  :root {
    --header-bg: #464444;
    --page-bg: #f3f3f4;
    --card-bg: #ffffff;
    --ink: #1c1c1c;
    --muted: #8a8a8a;
    --faint: #b3b3b3;
    --line: #e6e6e6;
    --accent: #2f73e0;
    --brand: #f2a33a;
    --band: #ececec;
    --button: #9a9a9a;
  }
  * { box-sizing: border-box; margin: 0; padding: 0; }
  html, body { width: 1200px; height: 798px; overflow: hidden; }
  body { font-family: "Lato", sans-serif; color: var(--ink); background: var(--page-bg); position: relative; }
  .abs { position: absolute; }

  .app-header { left: 0; top: 0; width: 1200px; height: 72px; background: var(--header-bg); color: #fff; }
  .brand { left: 23px; top: 27px; display: flex; align-items: center; gap: 6px; font-size: 10px; font-weight: 700; }
  .brand-dot { width: 16px; height: 16px; border-radius: 50%; background: var(--brand); }
  .header-divider { left: 188px; top: 4px; width: 1px; height: 64px; background: #5a5858; }
  .page-title { left: 207px; top: 26px; font-size: 17px; letter-spacing: .3px; }
  .page-subtitle { left: 207px; top: 46px; font-size: 11px; color: #9b9999; }
  .user { right: 24px; top: 24px; display: flex; align-items: center; gap: 8px; font-size: 17px; }

  .sidebar { left: 0; top: 72px; width: 189px; height: 726px; background: var(--card-bg); }
  .nav-item { left: 9px; font-size: 11px; display: flex; align-items: center; gap: 7px; }
  .nav-item svg { width: 12px; height: 12px; }
  .nav-section { left: 9px; font-size: 11px; width: 172px; display: flex; justify-content: space-between; }
  .campaign-band { left: 0; width: 189px; height: 23px; background: var(--band); display: flex; align-items: center; padding: 0 8px 0 7px; font-size: 11px; box-shadow: 0 2px 2px rgba(0,0,0,.08); }
  .campaign-band .chip { width: 15px; height: 15px; border-radius: 50%; background: #dcdcdc; margin-right: 9px; }
  .campaign-band .caret { margin-left: auto; width: 0; height: 0; border-left: 5px solid transparent; border-right: 5px solid transparent; }
  .caret.up { border-bottom: 5px solid #111; }
  .caret.down { border-top: 5px solid #111; }
  .sub-item { left: 33px; font-size: 11px; }
  .sub-active { left: 0; width: 189px; height: 22px; background: #f1f1f1; }
  .sub-item.active { color: var(--accent); font-weight: 700; }
  .collapse { left: 157px; top: 771px; font-size: 20px; font-weight: 700; letter-spacing: -3px; }

  .section-label { font-size: 11px; }
  .card { background: var(--card-bg); }
  .stat-box { border: 1px solid var(--line); display: flex; align-items: center; justify-content: center; gap: 10px; font-size: 27px; }
  .stat-box svg { width: 26px; height: 26px; }

  .avatar { left: 223px; top: 125px; width: 58px; height: 58px; border-radius: 50%; background: linear-gradient(135deg,#e2e2e2,#c9c9c9); }
  .campaign-title { left: 295px; top: 136px; font-size: 17px; }
  .campaign-desc { left: 295px; top: 161px; font-size: 9.5px; color: #555; }
  .customize { left: 1032px; top: 142px; width: 102px; height: 22px; background: var(--button); color: #fff; font-size: 9.5px; display: flex; align-items: center; justify-content: center; }

  .org-name { font-size: 11.5px; }
  .org-meta { font-size: 9px; color: var(--muted); }
  .hint { font-size: 11px; color: var(--faint); line-height: 1.3; }

  .footer-band { left: 189px; top: 753px; width: 1011px; height: 45px; background: linear-gradient(90deg,#3d3b3b,#4a4747,#3d3b3b); }
</style>
</head>
<body>
  <header class="app-header abs">
    <div class="brand abs"><span class="brand-dot"></span>PebbleLoop</div>
    <div class="header-divider abs"></div>
    <div class="page-title abs">Overview</div>
    <div class="page-subtitle abs">My Custom Campaign</div>
    <div class="user abs">
      <svg width="22" height="22" viewBox="0 0 22 22" fill="none" stroke="#fff" stroke-width="1.6"><circle cx="11" cy="11" r="10"/><circle cx="11" cy="8.5" r="3.5"/><path d="M4.5 17.5c1.6-2.6 3.9-3.6 6.5-3.6s4.9 1 6.5 3.6"/></svg>
      Username
    </div>
  </header>

  <nav class="sidebar abs">
    <div class="nav-item abs" style="top:14px"><svg viewBox="0 0 12 12" fill="none" stroke="#888"><path d="M1.5 6L6 1.8 10.5 6v4.5h-9z"/></svg>Home</div>
    <div class="nav-item abs" style="top:43px"><svg viewBox="0 0 12 12" fill="none" stroke="#888"><path d="M3 8.5V5.5a3 3 0 016 0v3l1 1H2zM5 10.5h2"/></svg>All alerts</div>
    <div class="nav-item abs" style="top:71px"><svg viewBox="0 0 12 12" fill="none" stroke="#888"><circle cx="6" cy="6" r="4.5"/><circle cx="6" cy="6" r="1.6"/></svg>Manage</div>
    <div class="nav-section abs" style="top:109px"><span>Campaigns</span><span>+</span></div>

    <div class="campaign-band abs" style="top:129px"><span class="chip"></span>My custom campaign<span class="caret up"></span></div>
    <div class="sub-active abs" style="top:158px"></div>
    <div class="sub-item active abs" style="top:162px">Overview</div>
    <div class="sub-item abs" style="top:190px">Files &amp; HoneyTokens</div>
    <div class="sub-item abs" style="top:219px">Resources</div>
    <div class="sub-item abs" style="top:247px">Alerts</div>
    <div class="sub-item abs" style="top:276px">Settings</div>
    <div class="campaign-band abs" style="top:308px"><span class="chip"></span>Default campaign<span class="caret down"></span></div>
    <div class="collapse abs" style="top:699px">&laquo;</div>
  </nav>

  <main>
    <div class="section-label abs" style="left:207px;top:95px">Campaign</div>
    <section class="card abs" style="left:206px;top:112px;width:973px;height:83px"></section>
    <div class="avatar abs" role="img" aria-label="Campaign settings illustration"></div>
    <div class="campaign-title abs">My Custom Campaign</div>
    <div class="campaign-desc abs">This is my custom campaign for finding ...</div>
    <div class="customize abs">Customize</div>

    <div class="section-label abs" style="left:208px;top:217px">Campaign organisation</div>
    <section class="card abs" style="left:206px;top:236px;width:973px;height:137px"></section>
    <svg class="abs" style="left:223px;top:252px" width="28" height="40" viewBox="0 0 28 40" fill="none" stroke="#222" stroke-width="1.3"><path d="M3 10l12-6v34H3zM15 4l9 5v29h-9"/><path d="M6 15h6M6 20h6M6 25h6M6 30h6M18 14h3M18 20h3M18 26h3"/></svg>
    <div class="org-name abs" style="left:267px;top:263px">Self-enabling Deliverables Proprietary Limited</div>
    <div class="org-meta abs" style="left:267px;top:278px">Standard</div>
    <div class="stat-box abs" style="left:221px;top:298px;width:211px;height:57px">
      <svg viewBox="0 0 26 26" fill="none" stroke="#222" stroke-width="1.2"><circle cx="13" cy="6" r="4"/><path d="M8 15c1-3 9-3 10 0M13 15v3M5 18h16"/><circle cx="5" cy="21" r="1.8"/><circle cx="13" cy="21" r="1.8"/><circle cx="21" cy="21" r="1.8"/><path d="M2 25h6M10 25h6M18 25h6"/></svg>
      86
    </div>
    <div class="org-name abs" style="left:702px;top:263px">Unleash bleeding-edge mindshare</div>
    <div class="org-meta abs" style="left:702px;top:278px">8 hours ago</div>
    <div class="stat-box abs" style="left:701px;top:298px;width:211px;height:57px">
      <svg viewBox="0 0 26 26" fill="none" stroke="#222" stroke-width="1.2"><rect x="10" y="3" width="6" height="5"/><path d="M13 8v5M4 13h18M4 13v5M13 13v5M22 13v5"/><rect x="1" y="18" width="6" height="5"/><rect x="10" y="18" width="6" height="5"/><rect x="19" y="18" width="6" height="5"/></svg>
      8
    </div>

    <div class="section-label abs" style="left:208px;top:397px">Files &amp; Honey Tokens</div>
    <section class="card abs" style="left:207px;top:417px;width:476px;height:134px"></section>
    <svg class="abs" style="left:226px;top:430px" width="28" height="30" viewBox="0 0 28 30" fill="none" stroke="#222" stroke-width="2"><path d="M9 4h15v20"/><rect x="3" y="8" width="16" height="20"/><path d="M7 15h8M7 19h8M7 23h8"/></svg>
    <div class="hint abs" style="left:265px;top:435px">Statistics</div>
    <div class="stat-box abs" style="left:224px;top:482px;width:210px;height:57px">
      <svg viewBox="0 0 26 26" fill="none" stroke="#222" stroke-width="1.5"><circle cx="13" cy="13" r="10"/><path d="M8 13l4 4 8-9"/></svg>
      0
    </div>
    <div class="stat-box abs" style="left:453px;top:482px;width:210px;height:57px">
      <svg viewBox="0 0 26 26" fill="none" stroke="#222" stroke-width="1.8"><path d="M9 3h13v17"/><rect x="4" y="7" width="14" height="17"/><path d="M8 13h6M8 16h6M8 19h6"/></svg>
      30
    </div>

    <div class="section-label abs" style="left:702px;top:397px">Resources</div>
    <section class="card abs" style="left:702px;top:417px;width:476px;height:134px"></section>
    <svg class="abs" style="left:717px;top:433px" width="30" height="30" viewBox="0 0 30 30" fill="none" stroke="#222" stroke-width="1.2"><rect x="2" y="2" width="12" height="12"/><rect x="16" y="2" width="12" height="12"/><rect x="2" y="16" width="12" height="12"/><rect x="16" y="16" width="12" height="12"/></svg>
    <div class="hint abs" style="left:759px;top:432px">Generate a collection of fictional organizations,<br>Custom templates, Uploaded files &amp; logos.</div>

    <div class="section-label abs" style="left:208px;top:575px">Alerts</div>
    <section class="card abs" style="left:207px;top:594px;width:476px;height:134px"></section>
    <svg class="abs" style="left:226px;top:610px" width="28" height="26" viewBox="0 0 28 26"><path d="M14 1L27 25H1z" fill="#111"/><path d="M14 9v8" stroke="#fff" stroke-width="2.4"/><circle cx="14" cy="21" r="1.4" fill="#fff"/></svg>
    <div class="hint abs" style="left:268px;top:615px">Alert statistics will appear here</div>
  </main>

  <footer class="footer-band abs" role="img" aria-label="Dark footer band with faint honeycomb pattern"></footer>
</body>
</html>
```